VORNAX Technologies Catalogue Design

We want the existing catalogue design to be completely re designed to have a better theme, that is professional and dynamic. we want the existing pictures changed, it would be great to have some images of local UAE population engaging in the activities shown. most of the written content remains the same. No.1 what we believe is to be removed. Point No. 3 all the little logos need to be re designed.

Target Market(s)

residential and corporate clients

Industry/Entity Type

home automation, command centers, audio video systems, lighting control systems

Requirements
Must have
• Point No. 3 all the little logos need to be re designed. Overall theme of the catalogue should look very good.
Nice to have
• Good font. Color theme can be related to logo which is black grey and red. Red maybe little less, leaving it to the designer to decide. it would be nice to have the cover of the catalogue clean and elegant. I have added doc of a pattern in blue color, it would be nice if it can be used as theme in the entire catalogue either in grey or black color, not blue.

```html
<!DOCTYPE html>
<html lang="en">
<head>
<meta charset="utf-8">
<title>VORNAX Technologies – Catalogue Cover</title>
<link href="https://fonts.googleapis.com/css2?family=Montserrat:wght@500;600;700;800&display=swap" rel="stylesheet">
<style>
  :root {
    --ink: #2b2727;
    --ink-soft: #3a3535;
    --red: #e0392b;
    --paper: #ffffff;
    --tab: #f2f2f2;
    --tab-shadow: rgba(0,0,0,0.18);
    --photo-a: #3d5a78;
    --photo-b: #8a98a6;
    --photo-c: #c9a640;
  }
  html, body { margin: 0; padding: 0; overflow: hidden; }
  body { width: 848px; height: 1200px; background: var(--paper); font-family: "Montserrat", sans-serif; }
  .cover { position: relative; width: 848px; height: 1200px; overflow: hidden; background: var(--paper); }
  .backdrop { position: absolute; inset: 0; }

  .brand { position: absolute; left: 66px; top: 62px; display: flex; align-items: center; gap: 14px; }
  .brand-mark { width: 34px; height: 34px; background: var(--red); }
  .brand-name { color: var(--ink); font-weight: 800; font-size: 24px; letter-spacing: 1px; line-height: 1; }
  .brand-name small { display: block; font-size: 9px; font-weight: 800; letter-spacing: 1.6px; margin-top: 5px; }

  .offer-list { position: absolute; left: 66px; top: 322px; margin: 0; padding: 0 0 0 12px; list-style: none;
    border-left: 3px solid var(--red); }
  .offer-list li { color: var(--ink); font-weight: 600; font-size: 18px; line-height: 28px; letter-spacing: 0.3px; }

  .services { position: absolute; right: 10px; top: 182px; width: 190px; margin: 0; padding: 0; list-style: none; }
  .service { position: relative; height: 64px; margin-bottom: 44px; display: flex; align-items: center; gap: 10px;
    padding-left: 26px; background: var(--tab);
    clip-path: polygon(14px 0, 100% 0, 100% 100%, 14px 100%, 0 50%);
    filter: drop-shadow(0 2px 3px var(--tab-shadow)); }
  .service svg { width: 30px; height: 30px; flex: none; }
  .service span { color: var(--ink); font-weight: 800; font-size: 11px; line-height: 13px; letter-spacing: 0.3px; }

  .badge { position: absolute; left: 468px; top: 812px; width: 150px; height: 134px; display: flex; flex-direction: column;
    align-items: center; justify-content: center; }
  .badge svg { position: absolute; inset: 0; }
  .badge .brand-mark { position: relative; width: 22px; height: 22px; margin-bottom: 6px; }
  .badge .brand-name { position: relative; font-size: 17px; text-align: center; }
  .badge .brand-name small { font-size: 6px; letter-spacing: 1px; margin-top: 3px; }
</style>
</head>
<body>
<main class="cover">
  <svg class="backdrop" width="848" height="1200" viewBox="0 0 848 1200">
    <defs>
      <linearGradient id="photo-tone" x1="0" y1="0" x2="1" y2="1">
        <stop offset="0" stop-color="var(--photo-b)"/>
        <stop offset="0.45" stop-color="var(--photo-a)"/>
        <stop offset="1" stop-color="#1e2a38"/>
      </linearGradient>
    </defs>
    <!-- top right dark sweep -->
    <path d="M640 0 C610 70 660 120 720 160 C790 205 812 260 812 330 L812 780 C812 800 830 810 848 810 L848 0 Z" fill="var(--ink)"/>
    <path d="M812 330 C812 260 790 205 720 160 C760 200 790 240 795 320 L795 800 L812 800 Z" fill="var(--red)"/>
    <path d="M620 0 C600 60 640 110 700 150" fill="none" stroke="var(--paper)" stroke-width="10"/>
    <!-- red wave -->
    <path d="M0 500 C120 470 240 520 320 560 L250 1200 L0 1200 Z" fill="var(--red)"/>
    <!-- dark lower body -->
    <path d="M0 540 C110 510 230 560 300 600 L340 1200 L0 1200 Z" fill="var(--ink)"/>
    <path d="M0 960 C200 930 420 980 600 930 C720 895 800 860 848 820 L848 1200 L0 1200 Z" fill="var(--ink)"/>
    <path d="M700 870 C760 850 810 820 848 790 L848 830 C810 860 760 885 700 900 Z" fill="var(--red)"/>
    <!-- photo frame -->
    <polygon points="265,540 537,540 668,760 537,980 265,980 136,760" fill="var(--red)"/>
    <polygon points="275,556 527,556 650,760 527,964 275,964 154,760" fill="var(--paper)"/>
    <polygon role="img" aria-label="Photo: engineer in a yellow hard hat working on a laptop in an industrial plant"
      points="283,570 519,570 634,760 519,950 283,950 170,760" fill="url(#photo-tone)"/>
  </svg>

  <div class="brand">
    <div class="brand-mark"></div>
    <div class="brand-name">VORNAX<small>TECHNOLOGIES L.L.C</small></div>
  </div>

  <ul class="offer-list">
    <li>ELV SYSTEMS</li>
    <li>AUDIO VISUAL</li>
    <li>HOME AUTOMATION</li>
    <li>EMERGING TECHNOLOGIES</li>
  </ul>

  <ul class="services">
    <li class="service">
      <svg viewBox="0 0 30 30" fill="none" stroke="var(--red)" stroke-width="2"><circle cx="15" cy="9" r="4"/><path d="M7 24 v-4 a8 8 0 0 1 16 0 v4 M4 26 h22"/></svg>
      <span>CONSULTANCY</span>
    </li>
    <li class="service">
      <svg viewBox="0 0 30 30" fill="none" stroke="var(--red)" stroke-width="2"><circle cx="15" cy="11" r="6"/><path d="M15 5 v-2 M15 17 v2 M9 11 h-2 M21 11 h2"/><rect x="4" y="21" width="7" height="6"/><rect x="19" y="21" width="7" height="6"/></svg>
      <span>PROJECT<br>MANAGEMENT</span>
    </li>
    <li class="service">
      <svg viewBox="0 0 30 30" fill="none" stroke="var(--red)" stroke-width="2"><circle cx="16" cy="10" r="5"/><path d="M3 22 h7 l5 3 h8 l5 -5"/></svg>
      <span>AMC SERVICE</span>
    </li>
    <li class="service">
      <svg viewBox="0 0 30 30" fill="none" stroke="var(--red)" stroke-width="2"><circle cx="15" cy="12" r="6"/><circle cx="15" cy="12" r="2"/><path d="M15 4 v2 M15 18 v2 M7 12 h2 M21 12 h2 M6 26 h18"/></svg>
      <span>SYSTEM<br>INTEGRATION</span>
    </li>
  </ul>

  <div class="badge">
    <svg viewBox="0 0 150 134"><polygon points="38,2 112,2 148,67 112,132 38,132 2,67" fill="var(--paper)" stroke="var(--ink)" stroke-width="2"/></svg>
    <div class="brand-mark"></div>
    <div class="brand-name">VORNAX<small>TECHNOLOGIES L.L.C</small></div>
  </div>
</main>
</body>
</html>
```